Business Card Design

We are a contracting firm, 95% of my work is interior renovations.... but also don't want to preclude the idea of doing exterior work if it arises. I Need a business card that says I am the ultimate professional. There is a per-determined notion that all contractors are shady, unreliable, etc. Being that most of my work is in Manhattan, I would like to give the impression of fresh, modern, sleek, design/build firm.

Target Market(s)

young couples 25-40

Industry/Entity Type

Business

Contact Information for Business Card

PeterHollowayInteriors LLC
27 North Brandel Street
Marsh Hollow NY 11492
718-555-0142
646-555-0187- cell
www.phbwx.com
ph@phbwx.com
Peter Holloway

Requirements
Should not have
• do not want to give the impression of a "bargain basement store"

```html
<!DOCTYPE html>
<html lang="en">
<head>
<meta charset="utf-8">
<title>Peter Holloway Interiors – Business Card</title>
<link rel="stylesheet" href="https://fonts.googleapis.com/css2?family=Libre+Baskerville&family=Didact+Gothic&display=swap">
<style>
  :root {
    --page: #d9d9d9;
    --card-dark: #1a1919;
    --card-dark-glow: #4a4848;
    --ink-light: #f2f2f2;
    --card-light: #ffffff;
    --band: #eef0f2;
    --band-deep: #e3e6e9;
    --ink-navy: #22324a;
    --ink-grey: #6d7178;
    --accent: #2a82c6;
  }
  * { margin: 0; padding: 0; box-sizing: border-box; }
  html, body { width: 1135px; height: 1200px; overflow: hidden; background: var(--page); }
  .sheet { position: relative; width: 1135px; height: 1200px; }

  .card {
    position: absolute; left: 117px; width: 900px; height: 514px;
    overflow: hidden; border-radius: 4px;
    box-shadow: 0 6px 18px rgba(0,0,0,0.18);
  }

  /* Front */
  .card-front {
    top: 56px;
    background: radial-gradient(ellipse 60% 55% at 50% 40%, var(--card-dark-glow), var(--card-dark) 75%);
    text-align: center;
  }
  .brand-name {
    position: absolute; top: 168px; left: 0; right: 0;
    font-family: "Libre Baskerville", serif; font-weight: 400;
    color: var(--ink-light); font-size: 46px; letter-spacing: 4px; line-height: 1.3;
    text-transform: uppercase;
  }
  .front-web {
    position: absolute; top: 402px; left: 0; right: 0;
    font-family: "Didact Gothic", sans-serif; color: var(--accent);
    font-size: 22px; letter-spacing: 5px;
  }

  /* Back */
  .card-back { top: 630px; background: var(--card-light); }
  .card-back svg.bands { position: absolute; inset: 0; }
  .person-name {
    position: absolute; top: 120px; left: 300px;
    font-family: "Libre Baskerville", serif; color: var(--ink-navy);
    font-size: 44px; letter-spacing: 4px; text-transform: uppercase;
    text-shadow: 0 3px 4px rgba(0,0,0,0.18);
  }
  .name-rule {
    position: absolute; top: 186px; left: 290px; width: 520px; height: 2px;
    background: linear-gradient(90deg, transparent, #b9bec4 20%, #b9bec4 80%, transparent);
  }
  .address {
    position: absolute; top: 250px; left: 62px;
    font-family: "Didact Gothic", sans-serif; color: var(--ink-grey);
    font-size: 19px; letter-spacing: 2px; line-height: 1.35;
    display: flex; gap: 12px;
  }
  .contacts {
    position: absolute; right: 58px; bottom: 50px;
    font-family: "Didact Gothic", sans-serif; color: var(--ink-grey);
    font-size: 21px; letter-spacing: 3px; line-height: 1.3; text-align: right;
    display: flex; gap: 14px; align-items: flex-end;
  }
  .contact-icons { display: flex; flex-direction: column; gap: 8px; padding-bottom: 3px; }
  .icon { width: 24px; height: 24px; display: block; }
</style>
</head>
<body>
<main class="sheet">

  <section class="card card-front" aria-label="Card front">
    <div class="brand-name">Peter Holloway<br>Interiors</div>
    <div class="front-web">www.phbwx.com</div>
  </section>

  <section class="card card-back" aria-label="Card back">
    <svg class="bands" width="900" height="514" viewBox="0 0 900 514" aria-hidden="true">
      <polygon points="0,40 900,200 900,300 0,120" fill="var(--band)"/>
      <polygon points="300,0 560,0 900,150 900,210" fill="var(--band-deep)" opacity="0.7"/>
      <polygon points="0,330 620,514 380,514 0,400" fill="var(--band)"/>
    </svg>

    <div class="person-name">Peter Holloway</div>
    <div class="name-rule"></div>

    <div class="address">
      <svg class="icon" viewBox="0 0 24 24" aria-hidden="true">
        <path d="M12 2a7 7 0 0 0-7 7c0 5 7 13 7 13s7-8 7-13a7 7 0 0 0-7-7z" fill="var(--accent)"/>
        <circle cx="12" cy="9" r="2.6" fill="#fff"/>
      </svg>
      <div>LLC 27 North<br>Brandel Street<br>Marsh Hollow<br>NY 11492</div>
    </div>

    <div class="contacts">
      <div>718 555 0142<br>646 555 0187<br>ph@phbwx.com<br>www.phbwx.com</div>
      <div class="contact-icons">
        <svg class="icon" viewBox="0 0 24 24" aria-hidden="true">
          <rect width="24" height="24" rx="4" fill="var(--accent)"/>
          <path d="M8 6l2 3-1.3 1.3a8 8 0 0 0 5 5L15 14l3 2-1 2.2c-5 0-10-5-10-10z" fill="#fff"/>
        </svg>
        <svg class="icon" viewBox="0 0 24 24" aria-hidden="true">
          <circle cx="12" cy="12" r="12" fill="var(--accent)"/>
          <rect x="6" y="8" width="12" height="8" fill="none" stroke="#fff" stroke-width="1.5"/>
          <path d="M6 8l6 5 6-5" fill="none" stroke="#fff" stroke-width="1.5"/>
        </svg>
        <svg class="icon" viewBox="0 0 24 24" aria-hidden="true">
          <circle cx="12" cy="12" r="12" fill="var(--accent)"/>
          <circle cx="12" cy="12" r="6.5" fill="none" stroke="#fff" stroke-width="1.4"/>
          <ellipse cx="12" cy="12" rx="2.8" ry="6.5" fill="none" stroke="#fff" stroke-width="1.2"/>
          <path d="M5.5 12h13" stroke="#fff" stroke-width="1.2"/>
        </svg>
      </div>
    </div>
  </section>

</main>
</body>
</html>
```